Redesign web application

we are a tele health start up. we need a new design for our platform that allows users, their family and docs to access their detailed stats online
users take readings using our wireless devices that transmit the readings to our server in the background All this happens in real time . and users can instantly login to the portal to view readings , make comments, , view charts,
if readings are not within in prescribed thresholds then alerts are reported on the website, SMS and email
please see the screenshots of existing pages
We need the following pages re designed
login page
patient DB summary , patient DB condition
Doc DB
Nurse DB
After you submit designs and we choose the winning design . please help to make minor modifications after that so that we can use it
Target Market(s)
Paying
Doctors/ Clinics/Clinic chains/ Specialists will be the ones who are paying for the service. the service
Non Paying
patients family members, doctors all will be accessing the system to view readings, alerts , make comments , see charts
Industry/Entity Type
Health
Colors
Look and feel

```html
<!DOCTYPE html>
<html lang="en">
<head>
<meta charset="utf-8">
<title>Telvanora – Sign in</title>
<link href="https://fonts.googleapis.com/css2?family=Hind:wght@400;500;600&display=swap" rel="stylesheet">
<style>
  :root {
    --bg-light: #eaf4fb;
    --bg-mid: #c9dff0;
    --bg-deep: #7fb0d6;
    --frame: rgba(205, 226, 238, 0.85);
    --card: #ffffff;
    --card-head: #e8f1f4;
    --ink: #2b3540;
    --ink-soft: #5c6873;
    --muted: #8f9aa5;
    --field-line: #d3d8dc;
    --icon: #c5ccd2;
    --accent: #22c3f8;
    --link: #12aee8;
  }
  * { box-sizing: border-box; margin: 0; padding: 0; }
  html, body { width: 1200px; height: 703px; overflow: hidden; }
  body {
    position: relative;
    font-family: "Hind", Arial, sans-serif;
    background: var(--bg-light);
    color: var(--ink);
  }
  .backdrop {
    position: absolute; inset: 0;
    background:
      radial-gradient(ellipse 260px 300px at 190px 250px, rgba(214,190,200,0.55), transparent 70%),
      radial-gradient(ellipse 340px 330px at 930px 240px, rgba(127,176,214,0.7), transparent 72%),
      linear-gradient(110deg, var(--bg-mid) 0%, var(--bg-light) 45%, #f0f7fc 100%);
  }
  .login-frame {
    position: absolute; left: 384px; top: 117px; width: 432px; height: 439px;
    background: var(--frame); border-radius: 6px;
  }
  .login-card {
    position: absolute; left: 392px; top: 125px; width: 416px; height: 424px;
    background: var(--card);
  }
  .card-head {
    height: 91px; background: var(--card-head);
    display: flex; align-items: center; justify-content: center; gap: 8px;
  }
  .brand-name { font-size: 27px; font-weight: 600; color: #111; letter-spacing: 0.2px; line-height: 1; padding-top: 4px; }
  .brand-mark { width: 18px; height: 18px; border: 2px solid #3b3fa6; }
  .card-title {
    position: absolute; top: 122px; left: 0; right: 0; text-align: center;
    font-size: 20px; font-weight: 400; color: var(--ink);
  }
  .field {
    position: absolute; left: 63px; width: 287px; height: 38px;
    border: 1px solid var(--field-line); display: flex; align-items: center;
    padding: 3px 13px 0; font-size: 12.5px; color: var(--muted);
  }
  .field svg { margin-left: auto; margin-top: -3px; }
  .field-email { top: 162px; }
  .field-password { top: 218px; }
  .remember {
    position: absolute; left: 63px; top: 274px; display: flex; align-items: center; gap: 9px;
    font-size: 13px; color: var(--ink-soft);
  }
  .remember-box { width: 15px; height: 15px; border: 1px solid var(--field-line); }
  .login-button {
    position: absolute; left: 63px; top: 308px; width: 287px; height: 38px;
    background: var(--accent); border-radius: 3px; color: #fff;
    font-size: 15px; font-weight: 500; display: flex; align-items: center; justify-content: center; padding-top: 2px;
  }
  .forgot { position: absolute; left: 62px; top: 362px; font-size: 12.5px; color: var(--muted); }
  .forgot a { color: var(--link); text-decoration: none; }
  .copyright {
    position: absolute; top: 571px; left: 0; right: 0; text-align: center;
    font-size: 12.5px; color: var(--ink-soft);
  }
</style>
</head>
<body>
  <div class="backdrop" role="img" aria-label="Soft blurred photo of a doctor with a stethoscope beside floating hexagon medical icons"></div>

  <div class="login-frame"></div>
  <main class="login-card">
    <header class="card-head">
      <span class="brand-name">Telvanora</span>
      <span class="brand-mark"></span>
    </header>

    <h1 class="card-title">Sign in to your account</h1>

    <div class="field field-email">
      <span>Email</span>
      <svg width="17" height="12" viewBox="0 0 17 12"><rect width="17" height="12" rx="1" fill="var(--icon)"/><path d="M0 1 L8.5 7 L17 1" stroke="#fff" stroke-width="1.3" fill="none"/></svg>
    </div>

    <div class="field field-password">
      <span>Password</span>
      <svg width="14" height="16" viewBox="0 0 14 16"><path d="M3.5 7 V4.5 a3.5 3.5 0 0 1 7 0 V7" stroke="var(--icon)" stroke-width="1.4" fill="none"/><rect x="1" y="7" width="12" height="8.5" rx="1" stroke="var(--icon)" stroke-width="1.4" fill="none"/><circle cx="7" cy="11" r="1.2" fill="var(--icon)"/></svg>
    </div>

    <label class="remember"><span class="remember-box"></span>Remember my email on this computer</label>

    <div class="login-button">Login Now</div>

    <p class="forgot">Forgot <a href="#">Username</a> / <a href="#">Password</a>?</p>
  </main>

  <footer class="copyright">Copyright 2014 © Telvanora. All Rights Reserved.</footer>
</body>
</html>
```